Landing pages for our website DataBeacon

We need 10 landing pages for:
1-KREV
1-PELUNEX
1-Cortavia
1-Vorn
3-Success Stories ( News, articles, interviews):
1-Demos Download
2- generical designs
Please find all the inspiration for the design on our website and the characteristics in the files attached.
https://databeacon-mx.example/
Technology and Artificial Intelligence elements to reflect our type of work.
Please consider our website as the main corporate image.
We have our main name of company Databeacon.
Secondary logo or branded service is: Cortaviar.
We need that the new templates are standardized with our actual image, please find examples of what we have received, that is what we expect.

Target Market(s)

Industrial users. Asset managers. Corporate visitors and customers.

Industry/Entity Type

Automotive. Chemical. Food and Beverage. Manufacturing

Font styles to use
Other font styles liked:
• Montserrat

Colors
0054AA
0677BA
7BADD7
CADEEF
E8F1F8

Requirements
Must have
• Use of our icon from the "cortavia" logo for the design of the template. Chips icons to connect equipments with software and control. Innovation
Nice to have
• Unique images, machine images. Connecting machines and data elements. Template version for google slides. Image for industrial software for control equipment and saving money to manufacturers. Segments: Automotive, Chemical, Food and Beverages, Mining and pharmaceutical, Energy Management
Should not have
• old elements

```html
<!DOCTYPE html>
<html lang="en">
<head>
<meta charset="utf-8">
<title>DataBeacon · Success Stories</title>
<link href="https://fonts.googleapis.com/css2?family=Poppins:ital,wght@0,400;0,500;0,600;0,700;1,400;1,500&display=swap" rel="stylesheet">
<style>
:root{
  --stage:#b3c7e2;
  --blue:#0054AA;
  --blue-mid:#0677BA;
  --blue-deep:#0a3d9f;
  --blue-bright:#1a5fd0;
  --sky:#7BADD7;
  --ice:#CADEEF;
  --mist:#E8F1F8;
  --ink:#1d1d1f;
  --text:#333;
  --grey:#f1f1f1;
  --slate:#2a2c30;
  --night:#15161b;
}
*{margin:0;padding:0;box-sizing:border-box}
html,body{width:1200px;height:2161px;overflow:hidden}
body{background:var(--stage);font-family:'Poppins',sans-serif;color:var(--text);position:relative}
.page{position:absolute;top:13px;width:520px;background:#fff;overflow:hidden}
.page--rounded{left:55px}
.page--angled{left:622px}
section{position:relative;width:100%;overflow:hidden}
.center{text-align:center}
p{font-size:7px;line-height:1.75}
.quote{font-style:italic}
.blue-text{color:var(--blue)}
.strong{font-weight:600}

/* header */
.hero{height:174px;background:linear-gradient(160deg,#1c1e2c 0%,#101118 55%,#0b0c12 100%);color:#fff}
.page--angled .hero{height:197px;background:linear-gradient(150deg,#0d3a8a 0%,#1650b5 40%,#0a2f78 100%)}
.page--angled .hero::after{content:"";position:absolute;left:0;right:0;bottom:0;height:26px;background:var(--slate);clip-path:polygon(0 0,100% 100%,0 100%)}
.page--angled .hero::before{content:"";position:absolute;left:0;right:0;bottom:0;height:26px;background:#fff;clip-path:polygon(0 55%,0 100%,100% 100%,100% 100%);z-index:1}
.nav{position:absolute;top:26px;left:32px;right:30px;display:flex;align-items:center}
.brand{font-size:13px;font-weight:500;letter-spacing:.3px;color:#fff;margin-right:auto}
.nav-links{display:flex;gap:13px;font-size:6px;color:#e6e6ea}
.lang{display:flex;align-items:center;gap:3px;margin-left:13px;font-size:6px;color:#fff}
.flag{width:8px;height:5px;background:linear-gradient(#c33 0 20%,#fff 20% 40%,#c33 40% 60%,#fff 60% 80%,#c33 80%);position:relative}
.flag::before{content:"";position:absolute;left:0;top:0;width:4px;height:3px;background:#2a3f8f}
.hero-title{position:absolute;top:82px;left:0;right:0;text-align:center}
.hero-title h1{font-size:18px;font-weight:600;letter-spacing:.4px}
.hero-title span{display:block;font-size:8.5px;margin-top:2px;color:#e8e8ee}

/* photo placeholders */
.photo{position:absolute}
.photo--handshake{background:linear-gradient(120deg,#d76b2c 0%,#c9a78a 35%,#9fb9d2 70%,#5f86b8 100%)}
.photo--vr{background:linear-gradient(135deg,#27364a 0%,#3f5f80 45%,#8fa84a 75%,#c8d84a 100%)}
.photo--engineer{background:linear-gradient(120deg,#7d8794 0%,#aab3bd 45%,#c7d35a 75%,#3c4a5e 100%)}
.photo--robotics{background:linear-gradient(135deg,#3a4d6e 0%,#5e7fb0 40%,#aab4c4 70%,#6a7482 100%)}
.photo--desk{background:linear-gradient(135deg,#e8e9eb 0%,#b9bec4 40%,#5d6a7d 75%,#30353d 100%)}
.photo--inspector{background:linear-gradient(130deg,#3e4a42 0%,#6b7560 40%,#c9d94a 65%,#2e3a36 100%)}
.illustration{position:absolute;background:radial-gradient(ellipse at 50% 60%,#f0c9e4 0%,#c79ae0 40%,#8a52c9 70%,#ffffff 100%)}
.round-right{border-radius:0 100px 100px 0}

/* left page sections */
.intro{height:187px}
.intro .photo{left:0;top:29px;width:255px;height:145px}
.intro-copy{position:absolute;left:266px;top:36px;width:225px}
.section-title{font-size:16px;font-weight:400;color:var(--ink);line-height:1.35}
.section-title b{color:var(--blue);font-weight:700}
.intro-copy p{margin-top:8px;color:var(--text)}
.intro-copy .section-title+p{margin-top:10px}

.lead{height:130px;padding:18px 40px 0}
.lead h3{font-size:9px;font-weight:600;color:var(--ink);line-height:1.75}
.lead .quote{font-size:7.5px;margin-top:12px;color:var(--text)}
.lead .blue-text{font-size:7.5px;margin-top:8px;font-weight:500}

.pill{position:absolute;background:var(--ice);border-radius:70px;padding:24px 34px 20px 36px;z-index:2}
.pill p{font-size:6.8px;line-height:2}
.listening{height:197px}
.listening .photo{left:267px;top:13px;width:253px;height:184px}
.listening .pill{left:33px;top:35px;width:257px;height:139px}

.network{height:136px;background:var(--grey);padding:30px 44px 0}
.network .quote{font-size:6.8px;color:var(--ink);line-height:2}
.network .blue-text{font-size:8.5px;font-weight:500;margin-top:8px;line-height:1.8}

.band{height:166px;background:linear-gradient(100deg,var(--blue-deep) 0%,var(--blue-bright) 55%,#1248ae 100%);color:#fff;display:flex;flex-direction:column;justify-content:center;padding:0 42px}
.band p{color:#fff;font-size:6.8px;line-height:1.9}
.band .quote+.quote{margin-top:8px}
.band .credit{font-style:normal;font-weight:500;font-size:7.2px;margin-top:4px}

.return{height:201px;background:var(--grey)}
.return .photo{left:0;top:32px;width:255px;height:144px}
.return .intro-copy{top:72px}

.sectors{height:220px}
.sectors .photo{left:268px;top:6px;width:252px;height:184px}
.sectors .pill{left:33px;top:29px;width:272px;height:138px;padding:26px 30px 20px 30px}
.sectors .pill .name{font-style:normal;font-weight:600;color:var(--ink);font-size:6.8px}
.sectors .pill .note{font-size:8px;color:var(--blue);font-weight:500;line-height:1.7;margin-top:8px}

.band--tall p{font-size:7.2px;line-height:2.1}
.impact{height:105px;background:var(--grey);display:flex;align-items:center;padding:0 44px}
.impact h3{font-size:9px;font-weight:600;color:var(--ink);line-height:1.8;text-align:center}

/* footer */
.footer{height:221px;background:#fff;padding:30px 32px 0;display:grid;grid-template-columns:136px 102px 118px 1fr;font-size:5.5px;color:var(--text)}
.footer-brand .name{font-size:14px;font-weight:500;color:var(--blue);display:block}
.footer-brand .name--sub{display:flex;align-items:center;gap:5px;margin-top:12px;color:var(--ink)}
.footer-brand .dot{width:10px;height:10px;border-radius:50%;background:var(--blue)}
.contact{margin-top:18px;list-style:none}
.contact li{display:flex;gap:6px;margin-bottom:6px;line-height:1.6}
.contact svg{flex:none;width:6px;height:6px;margin-top:1px}
.connect{margin-top:18px;color:#666}
.social{margin-top:14px;width:6px;height:6px;background:var(--blue)}
.footer h4{font-size:6.2px;font-weight:500;color:var(--blue);margin-bottom:10px}
.footer-nav{list-style:none}
.footer-nav li{margin-bottom:8px}
.footer-nav .work{margin-top:14px}
.post{margin-bottom:12px}
.post .t{color:#aaa;font-size:6px}
.post .d{font-size:4.6px;margin-top:2px}
.post .d span{color:var(--sky)}
.newsletter p{font-size:5.2px;line-height:1.7}
.newsletter label{display:block;margin-top:8px}
.field{width:100px;height:17px;border:1px solid #ccc;margin-top:3px}
.submit{display:inline-block;margin-top:8px;background:var(--blue);color:#fff;font-size:5px;font-weight:600;padding:5px 10px;letter-spacing:.3px}
.bottom-bar{height:28px;background:var(--night);color:#888;font-size:4.6px;display:flex;align-items:center;justify-content:center;position:relative}
.bottom-bar .up{position:absolute;right:40px;bottom:0;width:22px;height:10px;background:#2b2c33;border-radius:4px 4px 0 0;display:flex;align-items:center;justify-content:center}
.bottom-bar .zoom{position:absolute;right:6px;bottom:4px;color:#ccc;font-size:5px}

/* right page sections */
.r-intro{height:138px;padding:28px 40px 0}
.r-intro .section-title{font-size:16px}
.r-intro p{margin-top:10px;color:var(--text)}
.r-intro p+p{margin-top:6px}

.slab{background:var(--blue-deep);color:#fff}
.slab::before,.slab::after{content:"";position:absolute;left:0;right:0;height:20px;background:var(--slate);z-index:1}
.slab::before{top:0;clip-path:polygon(0 100%,100% 0,100% 0,100% 100%,0 100%)}
.slab::after{bottom:0;clip-path:polygon(0 0,100% 100%,0 100%)}
.slab .cap-top{position:absolute;top:0;left:0;right:0;height:20px;background:#fff;clip-path:polygon(0 0,100% 0,0 100%);z-index:2}
.slab .cap-bottom{position:absolute;bottom:0;left:0;right:0;height:20px;background:#fff;clip-path:polygon(100% 0,100% 100%,0 100%);z-index:2}
.slab p{color:#fff;font-size:6.8px;line-height:2}
.slab .plain{font-style:normal;line-height:1.8;margin-top:6px;font-size:7.2px}
.slab-copy{position:absolute;left:268px;width:222px}

.explain{height:287px}
.explain h3{position:absolute;top:38px;left:30px;right:30px;text-align:center;font-size:8.5px;font-weight:600;line-height:1.9;color:#fff}
.explain .photo{left:33px;top:88px;width:222px;height:160px}
.explain .slab-copy{top:118px}

.need{height:156px}
.need .copy{position:absolute;left:32px;top:32px;width:250px}
.need .copy p{font-size:7px;line-height:2.1}
.need .illustration{left:317px;top:30px;width:184px;height:108px}

.climb{height:239px}
.climb .photo{left:33px;top:37px;width:222px;height:160px}
.climb .slab-copy{top:54px}
.climb .slab-copy p.quote{font-size:6.5px}
.climb .plain{font-size:8px;line-height:1.7}

.manage{height:148px;padding:28px 38px 0}
.manage p{font-size:7px;line-height:2.1}
.manage .credit{font-style:normal;font-weight:500;color:var(--ink);margin-top:1px}
.r-return{height:92px;border-top:1px solid #e3e3e3;padding:18px 60px 0}
.r-return p{margin-top:6px}

.portfolio{height:239px}
.portfolio .photo{left:33px;top:37px;width:222px;height:160px}
.portfolio .slab-copy{top:72px}
.portfolio .name{font-style:normal;font-weight:600;font-size:6.8px}
.portfolio .plain{font-size:7.8px}

.allies{height:128px;padding:26px 34px 0}
.allies p{font-size:7.2px;line-height:2.1}
.r-impact{height:119px;background:linear-gradient(100deg,var(--blue-deep) 0%,var(--blue-bright) 60%,#1a52b8 100%);display:flex;align-items:center;padding:0 46px}
.r-impact h3{font-size:9px;font-weight:500;color:#fff;line-height:1.8;text-align:center}
.value{height:141px;background:var(--grey);padding:28px 38px 0}
.value p{font-size:7.2px;line-height:2.1}
.value p+p{margin-top:4px}
</style>
</head>
<body>

<!-- Page one: rounded layout -->
<div class="page page--rounded">
  <header class="hero">
    <nav class="nav">
      <span class="brand">DataBeacon</span>
      <div class="nav-links"><span>Solutions</span><span>Industries</span><span>Services</span><span>Innovation</span><span>Partners</span><span>Tech Allies</span><span>Demo</span></div>
      <div class="lang"><span class="flag"></span>EN</div>
    </nav>
    <div class="hero-title"><h1>Success Stories</h1><span>News, Articles, Interviews</span></div>
  </header>

  <section class="intro">
    <div class="photo photo--handshake round-right" role="img" aria-label="Handshake over a glowing industrial circuit backdrop"></div>
    <div class="intro-copy">
      <h2 class="section-title"><b>Databeacon:</b><br>Allies Of The Industry</h2>
      <p>During the last three decades, the role of Databeacon in industrial processes has been transformed from being a service provider to that of a strategic ally.</p>
      <p>With more than 4,000 projects carried out, its role has undoubtedly changed, as has its expertise on different processes.</p>
    </div>
  </section>

  <section class="lead center">
    <h3>They have obtained this thanks to a simple and useful practice: listening to the customer.<br>Leo Vargas, Director of Databeacon explains:</h3>
    <p class="quote">“Our way of understanding it has been to listen to the customer, visit the customer, see the plant, make suggestions, make changes. Sometimes they are very simple, but very significant.”</p>
    <p class="blue-text">And these, of course, generate savings in production, and better yet, profits.</p>
  </section>

  <section class="listening">
    <div class="photo photo--vr" role="img" aria-label="Technician with a VR headset operating a machine model on screens"></div>
    <div class="pill"><p class="quote blue-text">"The needs we attend to are, 'hey, let's connect a machine', 'and why do you want to connect that machine?', in a genuine listening process with the client, 'ah, because I need to generate a database', ' And why do you need a database?', 'Well, I have a request from the quality area', 'and the quality area, what is it asking you for?</p></div>
  </section>

  <section class="network center">
    <p class="quote">“We are climbing one by one, because they are different entities or actors. Then the quality people say, 'well, I need this database because I have to control the loss,' and then that loss is affecting us in more variables around the situation.”</p>
    <p class="blue-text">It is this internal knowledge of the plant, of its processes, that makes Databeacon an ally that offers a diagnosis and a profitable solution.</p>
  </section>

  <section class="band center">
    <p class="quote">“What we try to do is, at all levels, at each stage, in each need, obviously from the management to the operational part, make a system help them make a decision”</p>
    <p class="quote">“And they are often decisions of time, they are decisions of production attributes, they are decisions, incredibly logical. This process has led us to be more consultants, to be more helpers of what the condition of the plant is”,</p>
    <p class="credit">Explained Leo Vargas</p>
  </section>

  <section class="return">
    <div class="photo photo--engineer round-right" role="img" aria-label="Engineer with a laptop beside an industrial robot arm"></div>
    <div class="intro-copy">
      <h2 class="section-title"><b>Fast Return</b> On Investment</h2>
      <p>For 16 years, Databeacon has been key in modernizing the industry. In addition, his clients have recognized his role as an advisor.</p>
    </div>
  </section>

  <section class="sectors">
    <div class="photo photo--robotics" role="img" aria-label="Hands holding a tablet beside an automotive assembly line"></div>
    <div class="pill">
      <p class="quote blue-text">“The automotive, chemical, food and beverage sectors put us as a piece, perhaps even as a highly trusted area so that my operation is better,”</p>
      <p class="name">Said Leo Vargas</p>
      <p class="note">Of course they handle an interesting portfolio of solutions.</p>
    </div>
  </section>

  <section class="band band--tall center">
    <p class="quote">“We have our technological allies from the most influential part in the industrial segment. Now we can say that we have that support leadership, with a know-how of products, a know-how of attractive complex solutions. from the point of view, you make an investment and you have a return on investment, incredibly, sometimes in three or four months depending. It is not all, but we do bring an average of one year and three months of return on investment”</p>
  </section>

  <section class="impact">
    <h3>In the practices that Databeacon has had the most impact are those that concern energy consumption, be it in the management of assets, their failures, manufacturing time, and punctual compliance with quality, but lowering costs.</h3>
  </section>

  <section class="band band--tall center">
    <p class="quote">“We are going to help our clients to generate value, from the operational point of view, and that all that technology revolution, digital transformation, industry 4.0, any of those needs, now you land them with a project that you quickly get a return on.</p>
    <p class="quote">“First saving, then obtaining higher income, with a synchronization of work teams, of people, and not a useless expense,” said the head of Databeacon.</p>
  </section>

  <footer class="footer">
    <div class="footer-brand">
      <span class="name">DataBeacon</span>
      <span class="name name--sub"><span class="dot"></span>cortavia</span>
      <ul class="contact">
        <li><svg viewBox="0 0 10 10"><path d="M5 0a3.5 3.5 0 0 0-3.5 3.5C1.5 6 5 10 5 10s3.5-4 3.5-6.5A3.5 3.5 0 0 0 5 0z" fill="#0054AA"/></svg><span>Av. Central #120,<br>Col. Industrial</span></li>
        <li><svg viewBox="0 0 10 10"><rect x="0" y="2" width="10" height="6" fill="#0054AA"/></svg><span>info@databeacon-mx.example</span></li>
        <li><svg viewBox="0 0 10 10"><path d="M2 0l2 2-1 2 3 3 2-1 2 2-2 2C4 10 0 6 0 2z" fill="#0054AA"/></svg><span>+52 81 0000 4521</span></li>
      </ul>
      <p class="connect">Keep connected</p>
      <div class="social"></div>
    </div>
    <div>
      <h4>Navigation</h4>
      <ul class="footer-nav"><li>Solutions</li><li>Industries</li><li>Services</li><li>Innovation</li><li>Partners</li><li>Tech Allies</li><li>Demos</li><li>Language: 🇺🇸 ›</li><li class="work">Work with us</li></ul>
    </div>
    <div>
      <h4>Latest posts</h4>
      <div class="post"><div class="t">DBX2000 y 16 años de Databeacon</div><div class="d">November 10th, 2021 | <span>0 Comments</span></div></div>
      <div class="post"><div class="t">Bienvenido al internet industrial</div><div class="d">August 30th, 2021 | <span>0 Comments</span></div></div>
      <div class="post"><div class="t">Revolución Industrial 4.0</div><div class="d">August 30th, 2021 | <span>0 Comments</span></div></div>
    </div>
    <div class="newsletter">
      <h4>Newsletter</h4>
      <p>Subscribe and stay up to date with the most relevant information in the world of industrial automation.</p>
      <label>Email</label>
      <div class="field"></div>
      <span class="submit">SUBMIT</span>
    </div>
  </footer>
  <div class="bottom-bar">Copyright © DataBeacon | All rights reserved
    <span class="up"><svg width="5" height="4" viewBox="0 0 10 6"><path d="M1 5l4-4 4 4" stroke="#aaa" fill="none"/></svg></span><span class="zoom">x10</span>
  </div>
</div>

<!-- Page two: angled layout -->
<div class="page page--angled">
  <header class="hero">
    <nav class="nav">
      <span class="brand">DataBeacon</span>
      <div class="nav-links"><span>Solutions</span><span>Industries</span><span>Services</span><span>Innovation</span><span>Partners</span><span>Tech Allies</span><span>Demo</span></div>
      <div class="lang"><span class="flag"></span>EN</div>
    </nav>
    <div class="hero-title"><h1>Success Stories</h1><span>News, Articles, Interviews</span></div>
  </header>

  <section class="r-intro center">
    <h2 class="section-title"><b>Databeacon:</b> Allies Of The Industry</h2>
    <p>During the last three decades, the role of Databeacon in industrial processes has been transformed from being a service provider to that of a strategic ally.</p>
    <p>With more than 4,000 projects carried out, its role has undoubtedly changed, as has its expertise on different processes.</p>
  </section>

  <section class="slab explain">
    <span class="cap-top"></span><span class="cap-bottom"></span>
    <h3>They have obtained this thanks to a simple and useful practice: listening to the customer.<br>Leo Vargas, Director of Databeacon explains:</h3>
    <div class="photo photo--desk" role="img" aria-label="Support specialist with a headset working at a desktop computer"></div>
    <div class="slab-copy">
      <p class="quote">“Our way of understanding it has been to listen to the customer, visit the customer, see the plant, make suggestions, make changes. Sometimes they are very simple, but very significant.”</p>
      <p class="plain">And these, of course, generate savings in production, and better yet, profits.</p>
    </div>
  </section>

  <section class="need">
    <div class="copy"><p class="quote blue-text">"The needs we attend to are, 'hey, let's connect a machine', 'and why do you want to connect that machine?', in a genuine listening process with the client, 'ah, because I need to generate a database', ' And why do you need a database?', 'Well, I have a request from the quality area', 'and the quality area, what is it asking you for?</p></div>
    <div class="illustration" role="img" aria-label="Flat illustration of people working around a large data and gear server"></div>
  </section>

  <section class="slab climb">
    <span class="cap-top"></span><span class="cap-bottom"></span>
    <div class="photo photo--inspector" role="img" aria-label="Plant worker in hard hat and safety vest checking a tablet"></div>
    <div class="slab-copy">
      <p class="quote">“We are climbing one by one, because they are different entities or actors. Then the quality people say, 'well, I need this database because I have to control the loss,' and then that loss is affecting us in more variables around the situation.”</p>
      <p class="plain">It is this internal knowledge of the plant, of its processes, that makes Databeacon an ally that offers a diagnosis and a profitable solution.</p>
    </div>
  </section>

  <section class="manage center">
    <p class="quote blue-text">“What we try to do is, at all levels, at each stage, in each need, obviously from the management to the operational part, make a system help them make a decision”</p>
    <p class="quote blue-text">“And they are often decisions of time, they are decisions of production attributes, they are decisions, incredibly logical. This process has led us to be more consultants, to be more helpers of what the condition of the plant is”,</p>
    <p class="credit">Explained Leo Vargas</p>
  </section>

  <section class="r-return center">
    <h2 class="section-title"><b>Fast Return</b> On Investment</h2>
    <p>For 16 years, Databeacon has been key in modernizing the industry. In addition, his clients have recognized his role as an advisor.</p>
  </section>

  <section class="slab portfolio">
    <span class="cap-top"></span><span class="cap-bottom"></span>
    <div class="photo photo--robotics" role="img" aria-label="Hands holding a tablet beside an automotive assembly line"></div>
    <div class="slab-copy">
      <p class="quote">“The automotive, chemical, food and beverage sectors put us as a piece, perhaps even as a highly trusted area so that my operation is better,”</p>
      <p class="name">Said Leo Vargas</p>
      <p class="plain">Of course they handle an interesting portfolio of solutions.</p>
    </div>
  </section>

  <section class="allies center">
    <p class="quote blue-text">“We have our technological allies from the most influential part in the industrial segment. Now we can say that we have that support leadership, with a know-how of products, a know-how of attractive complex solutions. from the point of view, you make an investment and you have a return on investment, incredibly, sometimes in three or four months depending. It is not all, but we do bring an average of one year and three months of return on investment”</p>
  </section>

  <section class="r-impact">
    <h3>In the practices that Databeacon has had the most impact are those that concern energy consumption, be it in the management of assets, their failures, manufacturing time, and punctual compliance with quality, but lowering costs.</h3>
  </section>

  <section class="value center">
    <p class="quote blue-text">“We are going to help our clients to generate value, from the operational point of view, and that all that technology revolution, digital transformation, industry 4.0, any of those needs, now you land them with a project that you quickly get a return on.</p>
    <p class="quote blue-text">“First saving, then obtaining higher income, with a synchronization of work teams, of people, and not a useless expense,” said the head of Databeacon.</p>
  </section>

  <footer class="footer">
    <div class="footer-brand">
      <span class="name">DataBeacon</span>
      <span class="name name--sub"><span class="dot"></span>cortavia</span>
      <ul class="contact">
        <li><svg viewBox="0 0 10 10"><path d="M5 0a3.5 3.5 0 0 0-3.5 3.5C1.5 6 5 10 5 10s3.5-4 3.5-6.5A3.5 3.5 0 0 0 5 0z" fill="#0054AA"/></svg><span>Av. Central #120,<br>Col. Industrial</span></li>
        <li><svg viewBox="0 0 10 10"><rect x="0" y="2" width="10" height="6" fill="#0054AA"/></svg><span>info@databeacon-mx.example</span></li>
        <li><svg viewBox="0 0 10 10"><path d="M2 0l2 2-1 2 3 3 2-1 2 2-2 2C4 10 0 6 0 2z" fill="#0054AA"/></svg><span>+52 81 0000 4521</span></li>
      </ul>
      <p class="connect">Keep connected</p>
      <div class="social"></div>
    </div>
    <div>
      <h4>Navigation</h4>
      <ul class="footer-nav"><li>Solutions</li><li>Industries</li><li>Services</li><li>Innovation</li><li>Partners</li><li>Tech Allies</li><li>Demos</li><li>Language: 🇺🇸 ›</li><li class="work">Work with us</li></ul>
    </div>
    <div>
      <h4>Latest posts</h4>
      <div class="post"><div class="t">DBX2000 y 16 años de Databeacon</div><div class="d">November 10th, 2021 | <span>0 Comments</span></div></div>
      <div class="post"><div class="t">Bienvenido al internet industrial</div><div class="d">August 30th, 2021 | <span>0 Comments</span></div></div>
      <div class="post"><div class="t">Revolución Industrial 4.0</div><div class="d">August 30th, 2021 | <span>0 Comments</span></div></div>
    </div>
    <div class="newsletter">
      <h4>Newsletter</h4>
      <p>Subscribe and stay up to date with the most relevant information in the world of industrial automation.</p>
      <label>Email</label>
      <div class="field"></div>
      <span class="submit">SUBMIT</span>
    </div>
  </footer>
  <div class="bottom-bar">Copyright © DataBeacon | All rights reserved
    <span class="up"><svg width="5" height="4" viewBox="0 0 10 6"><path d="M1 5l4-4 4 4" stroke="#aaa" fill="none"/></svg></span><span class="zoom">x10</span>
  </div>
</div>

</body>
</html>
```